I need to refresh my meeting minutes pages (2 of them)

I have 2 pages that need to be modernized with a new look and feel. I have attached the 2 pages that need the refresh. I am okay with one page submissions as long as the winner is willing to add the second page before payment :-) Any questions please let me know. The logo on the page is not ours but a sample of what client may give us.

```html
<!DOCTYPE html>
<html lang="en">
<head>
<meta charset="utf-8">
<title>Meetings – ELSD</title>
<link href="https://fonts.googleapis.com/css2?family=Manrope:wght@400;500;600;700;800&display=swap" rel="stylesheet">
<style>
:root{
  --green:#0f6b2e;
  --ink:#111111;
  --muted:#6f6f6f;
  --line:#e6e6e6;
  --soft:#f6f6f6;
  --panel:#ffffff;
  --sidebar:#f7f7f7;
  --chip:#f2f2f2;
}
*{box-sizing:border-box;margin:0;padding:0}
html,body{width:1200px;height:872px;overflow:hidden;background:#fff}
body{font-family:"Manrope",sans-serif;color:var(--ink);position:relative}
svg{display:block}
.sidebar{position:absolute;left:0;top:0;width:208px;height:872px;background:var(--sidebar)}
.brand{position:absolute;left:21px;top:34px;font-size:23px;font-weight:800;color:var(--green);letter-spacing:.5px}
.sidebar-rule{position:absolute;left:20px;top:86px;width:168px;height:1px;background:var(--line)}
.nav{position:absolute;left:20px;top:120px;width:168px}
.nav-item{display:flex;align-items:center;gap:10px;height:39px;padding:0 12px;margin-bottom:10px;font-size:12.5px;font-weight:500;color:var(--ink);border-radius:8px}
.nav-item svg{width:18px;height:18px;stroke:#555;fill:none;stroke-width:1.5}
.nav-item.active{background:var(--green);color:#fff}
.nav-item.active svg{stroke:#fff}
.nav-badge{margin-left:auto;width:17px;height:17px;border-radius:50%;background:#fff;color:var(--green);font-size:8px;font-weight:700;display:flex;align-items:center;justify-content:center}

.topbar{position:absolute;left:208px;top:0;width:992px;height:88px;border-bottom:1px solid var(--line);background:var(--panel)}
.top-search{position:absolute;left:797px;top:28px;width:40px;height:40px;border-radius:50%;background:var(--chip);display:flex;align-items:center;justify-content:center}
.user-pill{position:absolute;left:832px;top:28px;width:125px;height:40px;border-radius:20px;background:var(--chip);display:flex;align-items:center;padding:0 8px;gap:10px;font-size:13px;font-weight:600}
.avatar{width:26px;height:26px;border-radius:50%;background:#e4e4e4;display:flex;align-items:center;justify-content:center;font-size:12px;font-weight:700}
.user-pill svg{margin-left:auto}

.list-panel{position:absolute;left:208px;top:88px;width:287px;height:784px;border-right:1px solid var(--line)}
.list-search{position:absolute;left:34px;top:27px;width:218px;height:40px;border:1px solid var(--line);border-radius:8px;display:flex;align-items:center;gap:10px;padding:0 13px;font-size:11.5px;color:var(--muted)}
.filter-btn{position:absolute;top:87px;height:40px;border:1px solid var(--line);border-radius:8px;display:flex;align-items:center;font-size:12px;font-weight:500}
.filter-featured{left:34px;width:77px;justify-content:center}
.filter-year{left:165px;width:87px;padding:0 12px;justify-content:space-between}
.scrollbar{position:absolute;left:270px;top:137px;width:4px;height:180px;border-radius:2px;background:#e8e8e8}
.meeting-list{position:absolute;left:0;top:147px;width:286px;list-style:none}
.meeting{height:74px;border-bottom:1px solid var(--line);padding:15px 34px 0 34px;font-size:12px}
.meeting:first-child{border-bottom:none}
.meeting.current{background:var(--soft);border-left:3px solid var(--green);padding-left:31px}
.meeting-row{display:flex;justify-content:space-between;margin-bottom:9px}
.meeting-date b{font-weight:700}
.meeting-title{font-weight:500}

.detail{position:absolute;left:495px;top:88px;width:705px;height:784px}
.icon-btn{position:absolute;top:27px;width:43px;height:40px;border:1px solid var(--line);border-radius:8px;display:flex;align-items:center;justify-content:center}
.detail-title{position:absolute;left:33px;top:100px;font-size:20px;font-weight:700}
.meta{position:absolute;top:148px;font-size:12.5px}
.meta-label{display:flex;align-items:center;gap:8px;color:var(--muted);margin-bottom:9px}
.meta-value{line-height:17px;font-weight:500}
.detail-rule{position:absolute;left:0;top:240px;width:705px;height:1px;background:var(--line)}
.detail-desc{position:absolute;left:33px;top:308px;width:630px;font-size:12px;line-height:17.5px;font-weight:500}
.actions{position:absolute;left:33px;top:376px;display:flex;gap:14px}
.action{height:40px;border-radius:8px;background:var(--soft);display:flex;align-items:center;gap:8px;padding:0 14px;color:var(--green);font-size:12.5px;font-weight:700}
.action svg{stroke:#555;fill:none;stroke-width:1.5}
</style>
</head>
<body>
<aside class="sidebar">
  <div class="brand">ELSD</div>
  <div class="sidebar-rule"></div>
  <nav class="nav">
    <div class="nav-item"><svg viewBox="0 0 24 24"><path d="M13 2 4 14h7l-1 8 9-12h-7z"/></svg>Featured</div>
    <div class="nav-item active"><svg viewBox="0 0 24 24"><circle cx="12" cy="8" r="3"/><circle cx="5" cy="10" r="2"/><circle cx="19" cy="10" r="2"/><path d="M6 19c0-3 3-5 6-5s6 2 6 5M2 18c0-2 1.5-3.5 3.5-3.5M22 18c0-2-1.5-3.5-3.5-3.5"/></svg>Meetings<span class="nav-badge">25</span></div>
    <div class="nav-item"><svg viewBox="0 0 24 24"><rect x="3" y="5" width="16" height="15" rx="2"/><path d="M3 10h16M8 3v4M14 3v4"/><circle cx="18" cy="18" r="3.5" fill="#f7f7f7"/></svg>Agenda</div>
    <div class="nav-item"><svg viewBox="0 0 24 24"><rect x="4" y="3" width="16" height="18" rx="2"/><path d="M8 8h8M8 12h8"/></svg>Policies</div>
  </nav>
</aside>

<header class="topbar">
  <div class="top-search"><svg width="18" height="18" viewBox="0 0 24 24" fill="none" stroke="#555" stroke-width="1.6"><circle cx="11" cy="11" r="7"/><path d="m20 20-4-4"/></svg></div>
  <div class="user-pill"><span class="avatar">S</span>Sam R.<svg width="12" height="12" viewBox="0 0 24 24" fill="none" stroke="#777" stroke-width="2"><path d="m6 9 6 6 6-6"/></svg></div>
</header>

<section class="list-panel">
  <div class="list-search"><svg width="18" height="18" viewBox="0 0 24 24" fill="none" stroke="#555" stroke-width="1.6"><circle cx="11" cy="11" r="7"/><path d="m20 20-4-4"/></svg>Search Meetings...</div>
  <div class="filter-btn filter-featured">Featured</div>
  <div class="filter-btn filter-year">2025<svg width="12" height="12" viewBox="0 0 24 24" fill="none" stroke="#777" stroke-width="2"><path d="m6 9 6 6 6-6"/></svg></div>
  <div class="scrollbar"></div>
  <ul class="meeting-list">
    <li class="meeting"><div class="meeting-row"><span class="meeting-date"><b>May 1, 2025</b> Thu</span><span>6:00 PM</span></div><div class="meeting-title">Special Meeting Agenda</div></li>
    <li class="meeting current"><div class="meeting-row"><span class="meeting-date"><b>Apr 24, 2025</b> Thu</span><span>6:00 PM</span></div><div class="meeting-title">Regular Meeting Agenda</div></li>
    <li class="meeting"><div class="meeting-row"><span class="meeting-date"><b>Apr 10, 2025</b> Thu</span><span>5:00 PM</span></div><div class="meeting-title">Special Meeting Agenda</div></li>
    <li class="meeting"><div class="meeting-row"><span class="meeting-date"><b>Mar 20, 2025</b> Thu</span><span>6:00 PM</span></div><div class="meeting-title">Special Meeting Agenda</div></li>
    <li class="meeting"><div class="meeting-row"><span class="meeting-date"><b>Mar 17, 2025</b> Thu</span><span>2:00 PM</span></div><div class="meeting-title">Special Meeting Agenda</div></li>
    <li class="meeting"><div class="meeting-row"><span class="meeting-date"><b>Mar 12, 2025</b> Thu</span><span>9:00 AM</span></div><div class="meeting-title">Special Meeting Agenda</div></li>
    <li class="meeting"><div class="meeting-row"><span class="meeting-date"><b>Mar 6, 2025</b> Thu</span><span>5:00 PM</span></div><div class="meeting-title">Special Meeting Agenda</div></li>
    <li class="meeting"><div class="meeting-row"><span class="meeting-date"><b>Feb 26, 2025</b> Thu</span><span>6:00 PM</span></div><div class="meeting-title">Special Meeting Agenda</div></li>
  </ul>
</section>

<main class="detail">
  <div class="icon-btn" style="left:33px"><svg width="14" height="14" viewBox="0 0 24 24" fill="none" stroke="#555" stroke-width="2"><path d="m15 6-6 6 6 6"/></svg></div>
  <div class="icon-btn" style="left:83px"><svg width="14" height="14" viewBox="0 0 24 24" fill="none" stroke="#555" stroke-width="2"><path d="m9 6 6 6-6 6"/></svg></div>
  <div class="icon-btn" style="left:628px"><svg width="18" height="18" viewBox="0 0 24 24" fill="none" stroke="#555" stroke-width="1.6"><path d="M14 5l7 6-7 6v-4c-5 0-8 1-11 5 1-6 4-9 11-10z"/></svg></div>
  <h1 class="detail-title">Regular Meeting Agenda</h1>
  <div class="meta" style="left:34px">
    <div class="meta-label"><svg width="17" height="17" viewBox="0 0 24 24" fill="none" stroke="#666" stroke-width="1.5"><rect x="3" y="5" width="18" height="16" rx="2"/><path d="M3 10h18M8 3v4M16 3v4M8 14h1M12 14h1M16 14h1M8 17h1M12 17h1"/></svg>Date</div>
    <div class="meta-value">Apr 24, 2025</div>
  </div>
  <div class="meta" style="left:174px">
    <div class="meta-label"><svg width="17" height="17" viewBox="0 0 24 24" fill="none" stroke="#666" stroke-width="1.5"><circle cx="12" cy="13" r="8"/><path d="M12 9v4l2 2M9 2h6"/></svg>Time</div>
    <div class="meta-value">6:00 PM</div>
  </div>
  <div class="meta" style="left:298px;width:380px">
    <div class="meta-label"><svg width="17" height="17" viewBox="0 0 24 24" fill="none" stroke="#666" stroke-width="1.5"><circle cx="12" cy="8" r="4"/><path d="M12 12v6M6 20h12"/></svg>Location</div>
    <div class="meta-value">Westbrook High School Media Center, 1800 North Maple Ridge Road, Fairview, Ohio 44210</div>
  </div>
  <div class="detail-rule"></div>
  <p class="detail-desc">This meeting is a meeting of the Board of Education in public for the purpose of conducting the District’s business. There is a time for public participation during the meeting as indicated in the agenda.</p>
  <div class="actions">
    <div class="action"><svg width="18" height="18" viewBox="0 0 24 24"><path d="M2 12s4-7 10-7 10 7 10 7-4 7-10 7S2 12 2 12z"/><circle cx="12" cy="12" r="3"/></svg>View</div>
    <div class="action"><svg width="18" height="18" viewBox="0 0 24 24"><path d="M6 2h9l4 4v16H6z"/><path d="M12 10v7M9 14l3 3 3-3"/></svg>Download PDF</div>
    <div class="action"><svg width="18" height="18" viewBox="0 0 24 24"><path d="M7 8V3h10v5M7 17H4V9h16v8h-3"/><rect x="7" y="14" width="10" height="7"/></svg>Print</div>
  </div>
</main>
</body>
</html>
```